KTW Ledgerwise Office Services Pty Ltd

Design a website for bookkeeping & accounting company

I like this website as an example with my own branding

https://go.quillcount.example/sydney-bookkeeping-lp/?keyword=bookkeeping%20sydney&matchtype=e&campaignid=482913057&device=c&adgroupid=31852064917&adposition=1t1&creative=607314928150&gclid=XkPwQrTbLmN3vZ8yHs5cDf2GaJ_uE0oWnRiYtBpKqLzMvXs_TeC

Number of Pages Required

1 page

Font styles to use
Sans Serif

Colors
9bcb3c

```html
<!DOCTYPE html>
<html lang="en">
<head>
<meta charset="utf-8">
<title>KTW Ledgerwise Office Services</title>
<link href="https://fonts.googleapis.com/css2?family=Montserrat:wght@400;500;600;700&display=swap" rel="stylesheet">
<style>
:root{
  --green:#9bcb3c;
  --navy:#1b1a8f;
  --red:#ee1b24;
  --ink:#222;
  --grey:#777;
  --light:#f4f4f4;
  --dark:#2b2d2f;
  --darker:#3a3a3a;
}
*{box-sizing:border-box;margin:0;padding:0}
html,body{width:1200px;height:3982px;overflow:hidden}
body{font-family:'Montserrat',sans-serif;color:var(--ink);background:#fff;position:relative}
section,header,footer{position:absolute;left:0;width:1200px}
.btn{display:inline-block;color:#fff;font-weight:600;text-align:center;border-radius:3px}

/* header */
.site-header{top:0;height:106px;background:#fff}
.brand{position:absolute;left:85px;top:30px;display:flex;align-items:center;gap:14px}
.brand-mark{font-size:44px;font-weight:700;letter-spacing:1px;color:var(--ink)}
.brand-name{font-size:12px;font-weight:600;line-height:15px;border-left:2px solid var(--ink);padding-left:12px;color:var(--ink);text-transform:uppercase}
.nav{position:absolute;right:90px;top:38px;display:flex;align-items:center;gap:30px;font-size:13px;font-weight:500;text-transform:uppercase}
.nav a{color:var(--ink);text-decoration:none}
.nav a.active{color:var(--navy);border-bottom:2px solid var(--navy);padding-bottom:4px}
.nav .btn{background:var(--red);padding:9px 16px;text-transform:none;font-size:13px}

/* hero */
.hero{top:106px;height:478px;background:var(--green)}
.hero-art{position:absolute;left:60px;top:40px;width:620px;height:400px;border-radius:6px;background:linear-gradient(135deg,#e8e6df,#c9c6bd 60%,#b3cf7a)}
.hero-copy{position:absolute;left:725px;top:78px;width:392px}
.hero-copy h1{font-size:28px;font-weight:600;line-height:37px;color:#fff;white-space:nowrap}
.hero-copy p{font-size:16px;font-weight:500;color:#222;margin:14px 0 20px;line-height:22px}
.field{height:40px;background:#fff;border-radius:3px;margin-bottom:14px;padding:11px 14px;font-size:13px;color:#555}
.hero-copy .btn{display:block;background:var(--navy);height:52px;line-height:52px;font-size:17px;font-weight:500}

/* about */
.about{top:584px;height:659px;background:#fff}
.section-title{text-align:center;font-size:31px;font-weight:500;line-height:42px;color:#333}
.about .section-title{padding-top:68px}
.feature{position:absolute;left:170px;width:430px;display:flex;gap:30px}
.feature-icon{flex:none;width:82px;height:82px;border-radius:50%;background:#e6e6e6;display:flex;align-items:center;justify-content:center}
.feature-icon.main{background:var(--navy)}
.feature h3{font-size:15px;font-weight:500;color:#555;margin:2px 0 8px}
.feature p{font-size:11.5px;line-height:19px;color:#999}
.about-art{position:absolute;left:640px;top:190px;width:460px;height:440px;border-radius:50%;background:radial-gradient(circle,#fafafa,#e9e9e9 70%,#fff 71%);display:flex;align-items:center;justify-content:center}
.about-art span{font-size:32px;font-weight:700;color:#222;background:#fff;border-radius:50%;width:120px;height:120px;line-height:120px;text-align:center}

/* services */
.services{top:1243px;height:1080px;background:var(--light)}
.services .section-title{padding-top:96px}
.rule{width:190px;height:2px;background:#bbb;margin:16px auto 0}
.grid{position:absolute;left:75px;top:180px;width:1050px;display:grid;grid-template-columns:repeat(3,1fr);row-gap:80px}
.service{text-align:center;padding:0 28px}
.service svg{display:block;margin:0 auto 12px}
.service h3{font-size:15px;font-weight:500;color:#333;margin-bottom:16px}
.service p{font-size:12px;line-height:19px;color:#555}
.services .cta{position:absolute;left:516px;top:930px;background:var(--red);width:238px;height:52px;line-height:52px;font-size:16px;font-weight:500}

/* banner */
.banner{top:2323px;height:266px;background:linear-gradient(90deg,#2a2c2e,#44474a 60%,#2f3133)}
.banner h2{position:absolute;left:178px;top:60px;width:660px;font-size:31px;font-weight:500;line-height:40px;color:#fff}
.banner p{position:absolute;left:180px;top:160px;width:560px;font-size:13px;line-height:20px;color:#eee}
.banner .btn{position:absolute;left:788px;top:146px;width:248px;height:54px;line-height:54px;background:var(--green);font-size:16px;font-weight:500}

/* clients */
.clients{top:2589px;height:186px;background:#fff;display:flex;justify-content:space-between;align-items:center;padding:0 110px}
.clients span{font-size:22px;font-weight:700;color:#222}

/* testimonial */
.testimonials{top:2775px;height:536px;background:var(--light)}
.testimonials .section-title{padding-top:52px;font-size:27px;font-weight:600}
.quote-card{position:absolute;left:152px;top:140px;width:460px;height:322px;background:#fff;padding:40px 40px}
.person{display:flex;align-items:center;gap:18px;margin-bottom:26px}
.avatar{width:90px;height:90px;border-radius:50%;background:linear-gradient(#d8d8d8,#9a9a9a)}
.person h3{font-size:23px;font-weight:500;color:var(--green)}
.person h4{font-size:16px;font-weight:600;color:var(--navy)}
.quote-card p{font-size:11.5px;line-height:19px;color:#555}
.video{position:absolute;left:612px;top:140px;width:400px;height:322px;background:linear-gradient(135deg,#1d2226,#3d4a55 55%,#1e262c)}
.video-title{position:absolute;left:12px;top:8px;font-size:12px;font-weight:500;color:#fff}
.video svg{position:absolute;left:170px;top:132px}

/* contact */
.contact{top:3311px;height:526px;background:linear-gradient(#202224,#2e3134)}
.map{position:absolute;left:85px;top:146px;width:472px;height:290px;background:linear-gradient(135deg,#e6e4de,#d6e0cc 55%,#e2e0da)}
.contact-info{position:absolute;left:612px;top:145px;width:500px;color:#fff}
.contact-info h2{font-size:29px;font-weight:500;color:var(--green);margin-bottom:18px}
.contact-info p{font-size:12.5px;line-height:20px;margin-bottom:22px}
.row{display:flex;font-size:14px;margin-bottom:18px;align-items:center}
.row b{width:100px;font-weight:500}
.row span{font-size:15px}
.socials{display:flex;gap:16px}
.socials i{width:16px;height:16px;border-radius:50%;background:#fff;display:block}

/* footer */
.site-footer{top:3837px;height:145px;background:var(--darker);color:#fff;font-size:13px;text-align:center;line-height:145px}
</style>
</head>
<body>

<header class="site-header">
  <div class="brand">
    <span class="brand-mark">KTW</span>
    <span class="brand-name">Ledgerwise<br>Office Services<br>Pty Ltd</span>
  </div>
  <nav class="nav">
    <a class="active">Home</a><a>Services</a><a>About</a><a>Contact</a>
    <a class="btn">Start A Free Trial</a>
  </nav>
</header>

<section class="hero">
  <div class="hero-art" role="img" aria-label="Team of business people drawing a rising colourful growth chart on a wall"></div>
  <div class="hero-copy">
    <h1>Free yourself With KTW<br>We'll do your Bookkeeping.</h1>
    <p>Australia's Largest Bookkeeping service for small businesse</p>
    <div class="field">Full Name</div>
    <div class="field">Email</div>
    <a class="btn">Start Your Free Trial</a>
  </div>
</section>

<section class="about">
  <h2 class="section-title">One of the largest bookkeeping<br>companies in Australia</h2>
  <div class="feature" style="top:200px">
    <div class="feature-icon main"><svg width="40" height="26" viewBox="0 0 40 26"><path d="M2 14l10-10 8 6 8-6 10 10-12 10-6-5-6 5z" fill="none" stroke="#fff" stroke-width="2.5"/></svg></div>
    <div><h3>Platinum Partner</h3><p>Certified on all major software packages including Tallyo (A Platinum Partner) Ledgra, Sumbook and more. No training required - we can start straight away.</p></div>
  </div>
  <div class="feature" style="top:352px">
    <div class="feature-icon"><svg width="36" height="36" viewBox="0 0 36 36" fill="#999"><circle cx="18" cy="18" r="5"/><circle cx="5" cy="10" r="3.5"/><circle cx="31" cy="10" r="3.5"/><circle cx="5" cy="27" r="3.5"/><circle cx="31" cy="27" r="3.5"/><path d="M5 10l13 8 13-8M5 27l13-9 13 9" stroke="#999" stroke-width="1.5"/></svg></div>
    <div><h3>Relationship</h3><p>Certified on all major software packages including Tallyo (A Platinum Partner) Ledgra, Sumbook and more. No training required - we can start straight away.</p></div>
  </div>
  <div class="feature" style="top:504px">
    <div class="feature-icon"><svg width="38" height="26" viewBox="0 0 38 26"><rect x="2" y="3" width="34" height="20" rx="2" fill="none" stroke="#999" stroke-width="2"/><circle cx="19" cy="13" r="5" fill="none" stroke="#999" stroke-width="2"/></svg></div>
    <div><h3>Secure Payment</h3><p>Certified on all major software packages including Tallyo (A Platinum Partner) Ledgra, Sumbook and more. No training required - we can start straight away.</p></div>
  </div>
  <div class="about-art" role="img" aria-label="Line drawing circle of office and accounting items: calculator, charts, documents, coins"><span>KTW</span></div>
</section>

<section class="services">
  <h2 class="section-title">How Can We Help?</h2>
  <div class="rule"></div>
  <div class="grid">
    <div class="service"><svg width="44" height="54" viewBox="0 0 44 54"><rect x="6" y="4" width="32" height="46" fill="none" stroke="#555" stroke-width="2"/><path d="M14 40V30M22 40V22M30 40V16" stroke="#555" stroke-width="3"/></svg><h3>Regular Reporting</h3><p>We can process your accounts from scratch based on bank statements, invoices and bills, keeping you up to date and on track.</p></div>
    <div class="service"><svg width="54" height="54" viewBox="0 0 54 54"><circle cx="27" cy="27" r="22" fill="none" stroke="#555" stroke-width="2"/><circle cx="27" cy="27" r="14" fill="none" stroke="#555" stroke-width="2"/><text x="27" y="33" font-size="16" text-anchor="middle" fill="#555" font-family="Montserrat,sans-serif">$</text></svg><h3>Bank Reconciliations</h3><p>We can process your accounts from scratch based on bank statements, invoices and bills, keeping you up to date and on track.</p></div>
    <div class="service"><svg width="44" height="54" viewBox="0 0 44 54"><rect x="6" y="4" width="32" height="46" fill="none" stroke="#555" stroke-width="2"/><path d="M12 16h20M12 24h20M12 32h20M12 40h12" stroke="#555" stroke-width="2"/></svg><h3>Payroll Services</h3><p>We can process your accounts from scratch based on bank statements, invoices and bills, keeping you up to date and on track.</p></div>
    <div class="service"><svg width="54" height="54" viewBox="0 0 54 54"><path d="M6 48h44M10 46V34M20 46V26M30 46V30M40 46V16M8 30l12-10 10 6 14-14" fill="none" stroke="#555" stroke-width="2.5"/></svg><h3>Regular Reporting</h3><p>We can process your accounts from scratch based on bank statements, invoices and bills, keeping you up to date and on track.</p></div>
    <div class="service"><svg width="58" height="54" viewBox="0 0 58 54"><rect x="4" y="6" width="50" height="34" fill="none" stroke="#555" stroke-width="2"/><path d="M22 48h14M29 40v8" stroke="#555" stroke-width="2"/><circle cx="29" cy="23" r="8" fill="none" stroke="#555" stroke-width="2"/></svg><h3>Accounts Payable &amp; Receivable</h3><p>We can process your accounts from scratch based on bank statements, invoices and bills, keeping you up to date and on track.</p></div>
    <div class="service"><svg width="44" height="54" viewBox="0 0 44 54"><rect x="8" y="12" width="28" height="38" fill="none" stroke="#555" stroke-width="2"/><circle cx="22" cy="12" r="8" fill="#fff" stroke="#555" stroke-width="2"/><path d="M22 26v14M16 34l6 6 6-6" fill="none" stroke="#555" stroke-width="2"/></svg><h3>Debtor Management</h3><p>We can process your accounts from scratch based on bank statements, invoices and bills, keeping you up to date and on track.</p></div>
    <div class="service"><svg width="54" height="54" viewBox="0 0 54 54"><rect x="8" y="4" width="34" height="40" fill="none" stroke="#555" stroke-width="2"/><path d="M14 14h22M14 22h22M14 30h14M4 50h46" stroke="#555" stroke-width="2"/></svg><h3>Online Bill Payments</h3><p>We can process your accounts from scratch based on bank statements, invoices and bills, keeping you up to date and on track.</p></div>
    <div class="service"><svg width="58" height="54" viewBox="0 0 58 54"><rect x="4" y="16" width="46" height="26" fill="none" stroke="#555" stroke-width="2"/><rect x="9" y="11" width="46" height="26" fill="#f4f4f4" stroke="#555" stroke-width="2"/><circle cx="32" cy="24" r="6" fill="none" stroke="#555" stroke-width="2"/></svg><h3>Cash Flow Management</h3><p>We can process your accounts from scratch based on bank statements, invoices and bills, keeping you up to date and on track.</p></div>
    <div class="service"><svg width="48" height="54" viewBox="0 0 48 54"><path d="M16 6h16l-5 9h-6z M10 50c-6-16 4-32 14-32s20 16 14 32z" fill="none" stroke="#555" stroke-width="2"/><text x="24" y="42" font-size="15" text-anchor="middle" fill="#555" font-family="Montserrat,sans-serif">$</text></svg><h3>Budgeting</h3><p>We can process your accounts from scratch based on bank statements, invoices and bills, keeping you up to date and on track.</p></div>
  </div>
  <a class="btn cta">Start Your Free Trial</a>
</section>

<section class="banner" role="img" aria-label="Dark toned photo of an office desk with paperwork and a laptop">
  <h2>Get in touch and we can fully customise an offering for you</h2>
  <p>We have offices all over Australia, but even if you aren't near an office we can still help you with your bookkeeping.</p>
  <a class="btn">Start Your Free Trial</a>
</section>

<section class="clients">
  <span>Swiftline</span><span>Everhour Gym</span><span>Vivace</span><span>Everhour Gym</span><span>Swiftline</span><span>Greenroot</span>
</section>

<section class="testimonials">
  <h2 class="section-title">What customers are saying about KTW</h2>
  <div class="quote-card">
    <div class="person">
      <div class="avatar" role="img" aria-label="Portrait photo of the client"></div>
      <div><h3>Marcus Elder</h3><h4>General Manager</h4></div>
    </div>
    <p>Marcus was looking for a solution that could be rolled out across various franchises easily. We wanted to make sure his franchisees could focus on running their businesses rather than worrying about admin. At KTW we worked with Marcus to outline a scalable solution that was easy to implement and low maintenance for franchisees - and most importantly, low cost!</p>
  </div>
  <div class="video" role="img" aria-label="Promotional video still of a smiling businessman in a suit">
    <div class="video-title">Free yourself With KTW We'll do your Bookkeeping.</div>
    <svg width="60" height="60" viewBox="0 0 60 60"><circle cx="30" cy="30" r="28" fill="#9bcb3c"/><path d="M24 18l18 12-18 12z" fill="#fff"/></svg>
  </div>
</section>

<section class="contact">
  <div class="map" role="img" aria-label="Street map showing the office location"></div>
  <div class="contact-info">
    <h2>Contact Us</h2>
    <p>We have offices all over Australia, but even if you aren't near an office we can still help you with your bookkeeping. Quillcount Bookkeeping started out in Sydney as Quillcount Bookkeeping.</p>
    <div class="row"><b>Address</b><span>14/52 Harbourne Way Kellyfield NSW 2999</span></div>
    <div class="row"><b>Phone No</b><span>0400 123 456</span></div>
    <div class="row"><b>Website</b><span>www.ktwledgerwise.example</span></div>
    <div class="row"><b>Follow Us</b><span class="socials"><i></i><i></i><i></i><i></i></span></div>
  </div>
</section>

<footer class="site-footer">© Copyright Ledgerwise Office Services 2018</footer>

</body>
</html>
```